Female Pest Controller needs awesome business cards

I need a logo design for a Pest Control service - something that appeals to 'nature' & safe, with the use of the colour green. I am also female
New Business Name is 'Bug Begone Bay'
appeals to women

Target Market(s)

Domestic Households & Local Businesses

Industry/Entity Type

Pest Control

Contact Information for Business Card

Corinne Waldrake
0428316952
ABN 47 618 259 304
PMT7314958207
Spiders Cockroaches, Ants, Silverfish, Fleas, Rodents

Font styles to use
Decorative

Colors
abd036
aaaaaa
5c5c5c

Requirements
Should not have
• Pics of dead insects, prefer nature inspired designs, frogs, trees etc
• Have attached old log & business name ( now my ex's business) Lilyvale Pest Solutions -

```html
<!DOCTYPE html>
<html lang="en">
<head>
<meta charset="utf-8">
<title>Bug Begone Bay – Business Card</title>
<link rel="stylesheet" href="https://fonts.googleapis.com/css2?family=Roboto:wght@400;500&family=Roboto+Condensed:wght@400&display=swap">
<style>
  :root {
    --page-bg: #ffffff;
    --card-bg: #f1f1f1;
    --card-edge: #e2e2e2;
    --brand-orange: #e2551f;
    --name-orange: #e4602a;
    --leaf-red: #c9451c;
    --leaf-amber: #e9a21f;
    --leaf-faint: #ead9c9;
    --grass-green: #3fa535;
    --water-blue: #9fd3df;
    --tag-green: #2f9a3a;
    --phone-green: #1f5a2a;
    --ink-dark: #233a25;
  }
  * { box-sizing: border-box; margin: 0; padding: 0; }
  html, body { width: 1200px; height: 900px; overflow: hidden; background: var(--page-bg); }
  .card {
    position: absolute; left: 120px; top: 170px; width: 960px; height: 560px;
    background: var(--card-bg); border-radius: 28px; overflow: hidden;
    border: 1px solid var(--card-edge);
    font-family: "Roboto", Arial, sans-serif;
  }
  .leaves { position: absolute; border-radius: 50%; }
  .leaves--top-left { left: -30px; top: -30px; width: 250px; height: 230px;
    background: radial-gradient(circle at 45% 45%, var(--leaf-red) 0%, var(--leaf-amber) 45%, rgba(233,162,31,0) 72%); }
  .leaves--mid-left { left: -60px; top: 290px; width: 210px; height: 230px;
    background: radial-gradient(circle at 45% 50%, var(--leaf-red) 0%, #e07a2a 42%, rgba(224,122,42,0) 72%); }
  .leaves--faint-bottom { left: 180px; top: 380px; width: 340px; height: 240px;
    background: radial-gradient(ellipse at center, var(--leaf-faint) 0%, rgba(234,217,201,0) 70%); }
  .leaves--right-column { right: -70px; top: -20px; width: 240px; height: 600px; border-radius: 40%;
    background: radial-gradient(ellipse at 60% 50%, var(--leaf-faint) 0%, rgba(234,217,201,0.6) 40%, rgba(234,217,201,0) 72%); }
  .leaves--right-amber { right: 20px; top: 360px; width: 130px; height: 130px;
    background: radial-gradient(circle, var(--leaf-amber) 0%, rgba(233,162,31,0) 70%); }
  .leaves--right-red { right: -20px; top: -10px; width: 110px; height: 110px;
    background: radial-gradient(circle, #a8461c 0%, rgba(168,70,28,0) 70%); }
  .logo-scene {
    position: absolute; left: 285px; top: 50px; width: 420px; height: 165px;
    border-radius: 40px 40px 60px 60px;
    background: linear-gradient(180deg, #7fc95a 0%, var(--grass-green) 55%, var(--water-blue) 100%);
    opacity: .9;
  }
  .brand, .contact { position: absolute; left: 0; width: 100%; text-align: center; line-height: 1.15; }
  .brand__name { top: 222px; font-size: 62px; font-weight: 400; color: var(--brand-orange); letter-spacing: 1px; }
  .brand__tagline { top: 310px; font-family: "Roboto Condensed", Arial, sans-serif; font-size: 19px; color: var(--tag-green); letter-spacing: 2px; }
  .contact__name { top: 345px; font-size: 36px; color: var(--name-orange); }
  .contact__phone { top: 398px; font-size: 36px; color: var(--phone-green); letter-spacing: 6px; }
  .contact__abn { top: 446px; font-size: 21px; font-weight: 500; color: var(--ink-dark); }
  .services {
    position: absolute; left: 60px; right: 40px; bottom: 28px; text-align: center;
    font-size: 20px; color: var(--tag-green); letter-spacing: 2px;
  }
</style>
</head>
<body>
  <div class="card">
    <div class="leaves leaves--top-left" role="img" aria-label="Autumn maple leaves"></div>
    <div class="leaves leaves--mid-left" role="img" aria-label="Autumn maple leaf"></div>
    <div class="leaves leaves--faint-bottom" role="img" aria-label="Faded maple leaves"></div>
    <div class="leaves leaves--right-column" role="img" aria-label="Faded maple leaves along the edge"></div>
    <div class="leaves leaves--right-amber" role="img" aria-label="Yellow maple leaf"></div>
    <div class="leaves leaves--right-red" role="img" aria-label="Brown maple leaf"></div>

    <div class="logo-scene" role="img" aria-label="Tree frog on a lily pad among grass and stones"></div>

    <div class="brand brand__name">Bug Begone Bay</div>
    <div class="brand brand__tagline">GENTLE PEST CARE FOR HOME AND GARDEN.</div>

    <div class="contact contact__name">Corinne Waldrake</div>
    <div class="contact contact__phone">0428316952</div>
    <div class="contact contact__abn">ABN 47 618 259 304</div>

    <div class="services">PMT LIC: SPIDERS COCKROACHES, ANTS, SILVERFISH, FLEAS, RODENTS</div>
  </div>
</body>
</html>
```